Corporate business card

Business card design for IT consultancy company.
Clients are larger companies.
Card should have round edges on some or all.
Make the user stop and look at the card.
Steel grey background. But if you have a better idea, show me.
Target Market(s)
Corporate - a but web 2.0
Industry/Entity Type
Business
Contact Information for Business Card
As per design.
Font styles to use
Other font styles liked:
- Helvetica
Colors
5c5c5c
ec2027
ffffff
Requirements
Must have
- Clean design - follow vorla styles
- text in white
- Lets have a conversation in red
- Powered by passion in red
Nice to have
- Uncluttered
Should not have
- Cluttered

```html
<!DOCTYPE html>
<html lang="en">
<head>
<meta charset="utf-8">
<title>Halden Group – Business Card</title>
<link rel="stylesheet" href="https://fonts.googleapis.com/css2?family=Open+Sans:wght@400;600;700;800&display=swap">
<style>
  :root {
    --steel-dark: #5c5c5c;
    --steel-mid: #9a9ea2;
    --steel-light: #c9cccf;
    --red: #ec2027;
    --white: #ffffff;
    --backdrop: #ececec;
  }
  * { margin: 0; padding: 0; box-sizing: border-box; }
  html, body {
    width: 1200px; height: 679px; overflow: hidden;
    background: var(--backdrop);
    font-family: "Open Sans", Helvetica, Arial, sans-serif;
  }
  .stage {
    position: relative; width: 1200px; height: 679px;
    display: flex; align-items: center; justify-content: center; gap: 80px;
  }
  .card {
    position: relative; width: 340px; height: 550px;
    border-radius: 26px; overflow: hidden;
    background:
      repeating-linear-gradient(0deg, rgba(255,255,255,0.06) 0 1px, rgba(0,0,0,0.04) 1px 3px),
      linear-gradient(160deg, var(--steel-light) 0%, var(--steel-mid) 55%, #8a8e92 100%);
    box-shadow: 0 6px 18px rgba(0,0,0,0.18);
  }
  .card__frame {
    position: absolute; inset: 9px;
    border: 3px solid var(--red); border-radius: 20px;
  }
  .front__brand {
    position: absolute; left: 34px; top: 44px;
    font-weight: 800; font-size: 40px; line-height: 1.05;
    color: var(--red); letter-spacing: 1px; text-transform: uppercase;
  }
  .front__person { position: absolute; left: 34px; top: 190px; }
  .person__name {
    font-weight: 700; font-size: 20px; color: var(--red);
    text-transform: uppercase; letter-spacing: 0.5px;
  }
  .person__role {
    font-size: 16px; color: var(--white);
    text-transform: uppercase; letter-spacing: 0.5px;
  }
  .contact-list {
    position: absolute; left: 34px; top: 275px; list-style: none;
  }
  .contact-list li {
    display: flex; align-items: center; gap: 12px;
    font-size: 17px; font-weight: 600; color: var(--white);
    height: 27px;
  }
  .contact-list svg { width: 16px; height: 16px; flex: none; }
  .front__tagline {
    position: absolute; left: 0; right: 0; bottom: 30px;
    text-align: center; font-weight: 700; font-size: 17px;
    color: var(--red); text-transform: uppercase; letter-spacing: 0.5px;
  }
  .back__watermark {
    position: absolute; left: 50%; top: 50%;
    transform: translate(-50%, -50%) rotate(-90deg);
    font-weight: 800; font-size: 110px; color: rgba(92,92,92,0.14);
    white-space: nowrap; letter-spacing: 6px;
  }
  .back__tagline {
    position: absolute; left: 50%; top: 50%;
    transform: translate(-50%, -50%) rotate(-90deg);
    font-weight: 600; font-size: 16px; color: var(--red);
    letter-spacing: 6px; white-space: nowrap; text-transform: uppercase;
  }
</style>
</head>
<body>
<main class="stage">
  <section class="card card--front">
    <div class="card__frame"></div>
    <div class="front__brand">Halden<br>Group</div>
    <div class="front__person">
      <p class="person__name">Daniel Marsh</p>
      <p class="person__role">Managing Partner</p>
    </div>
    <ul class="contact-list">
      <li><svg viewBox="0 0 16 16"><path fill="#ec2027" d="M4 1l3 3-1.5 2a8 8 0 0 0 4.5 4.5L12 9l3 3-2 2.5C7 14 2 9 1.5 3z"/></svg>+61390005522</li>
      <li><svg viewBox="0 0 16 16"><rect x="4" y="1" width="8" height="14" rx="1.5" fill="#ec2027"/><rect x="5.5" y="3" width="5" height="8" fill="#c9cccf"/></svg>0400555123</li>
      <li><svg viewBox="0 0 16 16"><rect x="1" y="3" width="14" height="10" rx="1.5" fill="#ec2027"/><path d="M1.5 4L8 9l6.5-5" stroke="#c9cccf" stroke-width="1.4" fill="none"/></svg>daniel@haldengroup.com.au</li>
      <li><svg viewBox="0 0 16 16"><circle cx="8" cy="8" r="7" fill="#ec2027"/></svg>daniel-marsh</li>
      <li><svg viewBox="0 0 16 16"><circle cx="8" cy="8" r="6.3" fill="none" stroke="#ec2027" stroke-width="1.6"/><path d="M1.7 8h12.6M8 1.7c-3 3.5-3 9 0 12.6M8 1.7c3 3.5 3 9 0 12.6" stroke="#ec2027" stroke-width="1.2" fill="none"/></svg>www.haldengroup.com.au</li>
    </ul>
    <p class="front__tagline">Lets have a conversation!</p>
  </section>

  <section class="card card--back">
    <div class="back__watermark" aria-hidden="true">HALDEN</div>
    <p class="back__tagline">Powered by passion!</p>
  </section>
</main>
</body>
</html>
```